Flyer-Design für Apotheke
Zielgruppe
Wir sind eine Apotheke, mit Schwerpunkt Mutter-Kind / Wiegenhafen Apotheke (www.wiegenhafen Apotheke)
Zielgruppe: Wir haben uns zertifiziert und spezialisiert im Bereich Mütter / Kinderwunsch / Stillen / Babys etc. (Siehe Anbei unser aktueller Entwurf Mutter-Kind-Broschüre)
Wir haben zahlreiche Handouts zu spezifischen Themen von der LHTV und unserem Verein Wiegenhafen Apotheken für unser Kunden schon fertig gestellt (siehe ein Beispiel im Anhang, auf dem wir noch unser Logo eingefügt haben).
Die Handouts sind meist 4-seitig A5, im Anhang mit unserem Logo noch versehen.
Zu zwei Themen möchten wir jetzt noch selbst ein Handout erstellen.
1) Fieberthermometer
2) Schnuller
Ziel: 4-6 Seiten, wir wollen es dann bei Druckfuchs drucken lassen.
Zielgruppe: Mütter, die zu uns in die Apotheke kommen und beraten werden (konkret in diesen Beispielen zum Thema Fieberthermometer bzw. Schnuller. Damit sie was mit nach Hause nehmen können, möchten wir die Handouts erstellen.
Texte anbei, Graphische Umsetzung ggf. mit netten Baby/Mütterbildern o.ä. erwünscht
Aufgabenstellung
Einbau Logo Tolvena-Apotheke (siehe Anhang) ähnlich wie auf dem Flyer Ernährung
(als Logo ohne Adresse etc. und irgendwo unter mit Adresse, Telefon etc.)
Logo Wiegenhafen Apotheke DARF NICHT MIT DRAUF

```html
<!DOCTYPE html>
<html lang="de">
<head>
<meta charset="utf-8">
<title>Fieberthermometer und -messung – Informationsbroschüre</title>
<link href="https://fonts.googleapis.com/css2?family=Roboto:wght@400;500;700;900&display=swap" rel="stylesheet">
<style>
  :root{
    --brand-red:#d40f1b;
    --ink:#1b1b1b;
    --body:#4a4a4a;
    --paper:#ffffff;
    --line:#d9d9d9;
    --cover-bg:#eef1f5;
  }
  *{box-sizing:border-box;margin:0;padding:0}
  html,body{width:1200px;height:567px;overflow:hidden;background:var(--paper)}
  body{font-family:"Roboto",Arial,sans-serif;color:var(--body)}
  .spread{position:relative;width:1200px;height:567px;border:1px solid var(--line);overflow:hidden}
  .panel{position:absolute;top:0;height:567px}
  .panel--inside{left:0;width:400px}
  .panel--back{left:400px;width:400px}
  .panel--cover{left:800px;width:400px;background:var(--paper)}
  .section-title{color:var(--brand-red);font-weight:500;font-size:16px;line-height:1.2;margin-bottom:8px}
  .copy{font-size:9.7px;line-height:13.3px;color:var(--body)}
  .copy + .copy{margin-top:13.3px}
  .hl{color:var(--brand-red)}
  .text-block{position:absolute;top:60px;left:27px;width:346px}
  .photo{position:absolute}
  .photo--mother{left:0;top:265px;width:400px;height:302px;
    background:linear-gradient(135deg,#e9e6e2 0%,#d8c2b4 40%,#b98f7a 70%,#8fb4d4 100%)}
  .photo--cover{left:0;top:0;width:400px;height:443px;
    background:linear-gradient(120deg,#f3f5f8 0%,#e7ebf0 45%,#e9c9b3 72%,#d9b09a 100%)}
  .brand{position:absolute;display:flex;align-items:center;gap:6px}
  .brand__name{font-weight:900;font-size:22px;color:var(--ink);letter-spacing:-.3px;white-space:nowrap}
  .brand__dot{width:14px;height:14px;border-radius:50%;background:var(--brand-red)}
  .panel--back .brand{left:123px;top:422px}
  .panel--cover .brand{left:137px;top:492px}
  .disclaimer{position:absolute;left:24px;top:528px;width:340px;font-size:6px;line-height:9.5px;color:#555}
  .cover-title{position:absolute;left:27px;top:71px;font-weight:700;font-size:24px;line-height:27px;color:var(--ink);letter-spacing:.2px}
  .tag{position:absolute;right:32px;top:0;height:20px;padding:0 8px;background:var(--brand-red);color:#fff;font-size:10.5px;line-height:20px;border-radius:0 0 7px 7px}
  .badge{position:absolute;left:30px;top:361px;width:122px;height:122px;border-radius:50%;background:var(--brand-red);color:#fff;text-align:center;transform:rotate(-6deg)}
  .badge__small{display:block;margin-top:30px;font-size:17px;font-weight:400;letter-spacing:.5px}
  .badge__big{display:block;font-size:40px;font-weight:900;line-height:40px}
</style>
</head>
<body>
<main class="spread">

  <section class="panel panel--inside">
    <div class="text-block">
      <h2 class="section-title">Fieberthermometer und -messung</h2>
      <p class="copy">Die Körpertemperatur des Menschen liegt <span class="hl">normalerweise</span> bei einem Wert um <span class="hl">37°C</span>. Dieser Wert variiert jedoch nicht nur individuell, sondern ist auch abhängig vom Tagesverlauf, Hormonen, Tagestemperatur, Stress und Schlaf. Hierbei können <span class="hl">Schwankungen von etwa 0,5 bis 1°C</span> entstehen, bei körperlicher Aktivität sogar Anstiege um bis zu 2°C. Grundsätzlich haben auch ältere Menschen niedrigere Körpertemperaturen als jüngere.</p>
      <p class="copy">Die gemessene Körpertemperatur hängt immer vom Ort der Messung ab. Hierbei wird prinzipiell zwischen zwei Temperaturzonen unterschieden: dem Körperkern und der Körperschale. Die Temperatur des Körperkerns liegt relativ konstant bei 37°C, die Körperschale ist abhängig von äußeren Einflüssen.</p>
    </div>
    <div class="photo photo--mother" role="img" aria-label="Foto: Mutter misst die Temperatur ihres Babys mit einem digitalen Fieberthermometer"></div>
  </section>

  <section class="panel panel--back">
    <div class="text-block">
      <h2 class="section-title">Fazit</h2>
      <p class="copy">Die genauste Methode der Fiebermessung ist die rektale Messung. Besonders bei Neugeborenen und Kindern mit Fieberkrämpfen ist diese zu bevorzugen. Sollte sie nicht durchführbar sein, ist die Messung am Ohr besonders für Kinder eine geeignete Alternative. Hier ist jedoch ebenfalls wie beim Stirnthermometer der geübte Umgang und der Temperaturunterschied zur Körperkerntemperatur zu beachten. Daher empfiehlt es sich nach Kauf des Messinstrumentes die individuelle, gesunde Körpertemperatur zu bestimmen. Die Messung unter den Achseln ist wegen hoher Temperaturabweichungen generell nicht zu empfehlen.</p>
      <p class="copy">Bei weiteren Fragen helfen wir Ihnen gerne weiter.</p>
      <p class="copy">Ihr babyfreundliches Team der Tolvena Apotheke Lindwerth</p>
    </div>
    <div class="brand"><span class="brand__name">Tolvena Apotheke</span><span class="brand__dot"></span></div>
    <p class="disclaimer">Die vorliegenden Informationen wurden mit größtmöglicher Sorgfalt nach dem derzeitigen aktuellen Stand der Wissenschaft zusammengestellt, dennoch übernehmen Verfasser und Herausgeber keine Gewähr.<br>Es besteht kein Anspruch auf Vollständigkeit.</p>
  </section>

  <section class="panel panel--cover">
    <div class="photo photo--cover" role="img" aria-label="Foto: Baby bekommt ein Fieberthermometer in den Mund"></div>
    <div class="tag">Informationsbroschüre</div>
    <h1 class="cover-title">FIEBERTHERMOMETER<br>UND -MESSUNG</h1>
    <div class="badge"><span class="badge__small">Gewusst,</span><span class="badge__big">WIE!</span></div>
    <div class="brand"><span class="brand__name">Tolvena Apotheke</span><span class="brand__dot"></span></div>
  </section>

</main>
</body>
</html>
```